Images for Homepage of Recruiting website
Our Database of IT Professionals
none
We're an IT Recruiting company in Houston and I want to have some images of graphs/charts/speedometers of the type and number of candidates we have in our database.
Advertising
Target is for clients to see the type of talent we recruit.
I attached several documents that should help understand the size I need. You may be able to get creative and get all the data into one image but if not expand it to another image. I will have this image rotating with some others on my homepage.
This image shows the size of images I need
Shows the data I want to represent via graphs/charts/speedometers/etc...
very rough examples of what i'm looking for

```html
<!DOCTYPE html>
<html lang="en">
<head>
<meta charset="utf-8">
<title>Candidate Source</title>
<link href="https://fonts.googleapis.com/css2?family=Cinzel:wght@400;600;700&display=swap" rel="stylesheet">
<style>
  :root {
    --bg-light: #f4f4f4;
    --bg-mid: #d9d9d9;
    --bg-dark: #bdbdbd;
    --ink: #333333;
    --referral: #0d3351;
    --social: #1fa9ea;
    --other: #1a80c6;
    --white: #ffffff;
    --label: #111111;
    --brand: #6a6a6a;
    --brand-dot: #8cc63f;
  }
  * { margin: 0; padding: 0; box-sizing: border-box; }
  html, body { width: 1200px; height: 391px; overflow: hidden; background: var(--white); }
  .banner {
    position: relative;
    width: 1200px;
    height: 391px;
    overflow: hidden;
    background:
      linear-gradient(115deg, transparent 0 30%, rgba(255,255,255,.7) 34%, transparent 40%),
      linear-gradient(100deg, transparent 0 55%, rgba(255,255,255,.5) 60%, transparent 66%),
      linear-gradient(90deg, var(--bg-light) 0%, var(--bg-mid) 55%, var(--bg-dark) 100%);
    font-family: "Cinzel", serif;
  }
  .chart { position: absolute; left: 0; top: 0; }
  .chart text { font-family: "Cinzel", serif; }
  .pct { fill: var(--white); font-size: 26px; font-weight: 600; }
  .label { fill: var(--label); font-size: 24px; font-weight: 700; letter-spacing: 1px; }
  .leader { stroke: var(--label); stroke-width: 2; fill: none; }
  .title {
    position: absolute;
    left: 0;
    top: 30px;
    color: var(--ink);
    text-shadow: 2px 2px 3px rgba(0,0,0,.25);
    line-height: 1;
    font-weight: 600;
  }
  .title-line { display: block; letter-spacing: 2px; white-space: nowrap; }
  .title-line--top { font-size: 70px; padding-left: 70px; }
  .title-line--bottom { font-size: 92px; padding-left: 18px; margin-top: -6px; }
  .brand {
    position: absolute;
    left: 130px;
    top: 228px;
    display: flex;
    align-items: center;
    gap: 12px;
  }
  .brand-name {
    font-family: "Cinzel", serif;
    font-weight: 700;
    font-size: 36px;
    color: var(--brand);
  }
  .brand-dot { width: 22px; height: 22px; border-radius: 50%; background: var(--brand-dot); }
</style>
</head>
<body>
<div class="banner">
  <svg class="chart" width="1200" height="391" viewBox="0 0 1200 391" aria-label="Donut chart of candidate sources: Referral 80%, ProfileNet 10%, Other 10%">
    <circle class="slice slice--referral" cx="760" cy="247" r="225" fill="none" stroke="var(--referral)" stroke-width="150"/>
    <path class="slice slice--social" fill="var(--social)" stroke="var(--white)" stroke-width="3"
      d="M852.7,-38.3 A300 300 0 0 1 1002.7,70.6 L881.4,158.8 A150 150 0 0 0 806.4,104.3 Z"/>
    <path class="slice slice--other" fill="var(--other)" stroke="var(--white)" stroke-width="3"
      d="M1002.7,70.6 A300 300 0 0 1 1060,247 L910,247 A150 150 0 0 0 881.4,158.8 Z"/>
    <circle class="hole" cx="760" cy="247" r="150" fill="var(--white)"/>

    <text class="pct" x="550" y="258" text-anchor="middle">80%</text>
    <text class="pct" x="882" y="100" text-anchor="middle">10%</text>
    <text class="pct" x="982" y="212" text-anchor="middle">10%</text>

    <text class="label" x="1178" y="50" text-anchor="end">ProfileNet</text>
    <polyline class="leader" points="934,80 962,60 1180,60"/>

    <text class="label" x="1178" y="162" text-anchor="end">Other</text>
    <polyline class="leader" points="1022,192 1048,172 1180,172"/>

    <text class="label" x="662" y="256">Referral</text>
    <line class="leader" x1="594" y1="266" x2="796" y2="266"/>
  </svg>

  <h1 class="title">
    <span class="title-line title-line--top">Candidate</span>
    <span class="title-line title-line--bottom">Source</span>
  </h1>

  <div class="brand">
    <span class="brand-name">brightfolio</span>
    <span class="brand-dot"></span>
  </div>
</div>
</body>
</html>
```